Parkinson's Disease Progression

Visually describe the rate of Parkinson progression in the first 15 years following diagnosis. Title: "Patient-Perceived Progression of Parkinsonism"

The attached figure names "meanqol" is the curve that should serve as the basis of this graphic. Everything else-- color, labels, font, etc. describe this curve.
Thank you!

Target Market(s)

People with Parkisnon's Disease, neurologists, family members.

Font styles to use
Sans Serif

Requirements
Must have
• Must have the lines going through these exact numbers
Excellent -- 502
Very good- 661
Good- 895
Fair- 1268
Poor- 1655

LABELS:
Title: "Patient-Perceived Progression of Parkinsonism"
"SAW-MX (Self-Assessed Wellbeing Index for Movement Conditions)" should be the label on the left.
"Quality of Life" should be the label on the right
"Years Since Diagnosis" should be the label on the bottom
Nice to have
• A color scheme that goes from GOOD (low numbers) to BAD (high numbers).

Easy to read (elderly)

```html
<!DOCTYPE html>
<html lang="en">
<head>
<meta charset="UTF-8">
<title>Patient-Perceived Progression of Parkinsonism</title>
<link rel="stylesheet" href="https://fonts.googleapis.com/css2?family=Barlow+Condensed:wght@500;600;700&family=Barlow+Semi+Condensed:wght@500&family=Montserrat:wght@400&display=swap">
<style>
  :root {
    --ink-title: #0b2496;
    --ink-axis: #6b6b6b;
    --ink-label: #7a7a7a;
    --grid: #e1e2e4;
    --baseline: #4a4c58;
    --curve: #bdbdbd;
    --frame: #2a2a2a;
    --bg-center: #ffffff;
    --bg-edge: #eceeef;
    --excellent: #f9b52c;
    --very-good: #f5599a;
    --good: #e453e8;
    --fair: #7e2ae6;
    --poor: #9424b0;
  }
  html, body {
    margin: 0;
    padding: 0;
    overflow: hidden;
    background: #ffffff;
  }
  .canvas {
    position: relative;
    width: 1200px;
    height: 859px;
    box-sizing: border-box;
    border: 1px solid var(--frame);
    background: radial-gradient(ellipse at 50% 48%, var(--bg-center) 30%, var(--bg-edge) 100%);
    overflow: hidden;
  }
  .chart {
    position: absolute;
    inset: 0;
    width: 1200px;
    height: 859px;
  }
  .chart-title {
    font-family: "Barlow Semi Condensed", sans-serif;
    font-weight: 500;
    font-size: 37px;
    fill: var(--ink-title);
  }
  .tick-label {
    font-family: "Barlow Condensed", sans-serif;
    font-weight: 600;
    font-size: 21px;
    fill: var(--ink-axis);
  }
  .value-label {
    font-family: "Barlow Condensed", sans-serif;
    font-weight: 700;
    font-size: 47px;
  }
  .category-label {
    font-family: "Barlow Condensed", sans-serif;
    font-weight: 600;
    font-size: 27px;
    fill: #ffffff;
  }
  .axis-acronym {
    font-family: "Montserrat", sans-serif;
    font-weight: 400;
    font-size: 37px;
    fill: var(--ink-label);
  }
  .axis-name {
    font-family: "Montserrat", sans-serif;
    font-weight: 400;
    font-size: 20.5px;
    fill: var(--ink-label);
  }
  .axis-right, .axis-bottom {
    font-family: "Montserrat", sans-serif;
    font-weight: 400;
    font-size: 26px;
    fill: var(--ink-label);
  }
  .gridline { stroke: var(--grid); stroke-width: 1.2; }
  .baseline { stroke: var(--baseline); stroke-width: 5; stroke-linecap: round; }
  .axis-rule { stroke: var(--ink-axis); stroke-width: 1.4; }
  .trend { fill: none; stroke: var(--curve); stroke-width: 2.5; }
</style>
</head>
<body>
<main class="canvas">
<svg class="chart" viewBox="0 0 1200 859" xmlns="http://www.w3.org/2000/svg" role="img" aria-label="Bar chart of patient-perceived progression of parkinsonism by quality of life rating">
  <defs>
    <linearGradient id="fill-excellent" x1="0" y1="0" x2="0.4" y2="1">
      <stop offset="0" stop-color="#fbc52c"/><stop offset="1" stop-color="#f28535"/>
    </linearGradient>
    <linearGradient id="fill-very-good" x1="0" y1="0" x2="0.4" y2="1">
      <stop offset="0" stop-color="#ff7f9e"/><stop offset="1" stop-color="#f41b98"/>
    </linearGradient>
    <linearGradient id="fill-good" x1="0" y1="0" x2="0.3" y2="1">
      <stop offset="0" stop-color="#ff66dc"/><stop offset="1" stop-color="#b72ae0"/>
    </linearGradient>
    <linearGradient id="fill-fair" x1="0" y1="0" x2="0.3" y2="1">
      <stop offset="0" stop-color="#8a30e4"/><stop offset="1" stop-color="#5208e6"/>
    </linearGradient>
    <linearGradient id="fill-poor" x1="0" y1="0" x2="0.2" y2="1">
      <stop offset="0" stop-color="#a226b6"/><stop offset="1" stop-color="#52188e"/>
    </linearGradient>
  </defs>

  <text class="chart-title" x="672" y="85" text-anchor="middle">Patient-Perceived Progression of Parkinsonism</text>

  <g class="grid">
    <line class="gridline" x1="258" x2="1094" y1="109.5" y2="109.5"/>
    <line class="gridline" x1="258" x2="1094" y1="134.2" y2="134.2"/>
    <line class="gridline" x1="258" x2="1094" y1="158.8" y2="158.8"/>
    <line class="gridline" x1="258" x2="1094" y1="183.5" y2="183.5"/>
    <line class="gridline" x1="258" x2="1094" y1="208.1" y2="208.1"/>
    <line class="gridline" x1="258" x2="1094" y1="232.8" y2="232.8"/>
    <line class="gridline" x1="258" x2="1094" y1="257.4" y2="257.4"/>
    <line class="gridline" x1="258" x2="1094" y1="282.1" y2="282.1"/>
    <line class="gridline" x1="258" x2="1094" y1="306.7" y2="306.7"/>
    <line class="gridline" x1="258" x2="1094" y1="331.4" y2="331.4"/>
    <line class="gridline" x1="258" x2="1094" y1="356" y2="356"/>
    <line class="gridline" x1="258" x2="1094" y1="380.7" y2="380.7"/>
    <line class="gridline" x1="258" x2="1094" y1="405.3" y2="405.3"/>
    <line class="gridline" x1="258" x2="1094" y1="430" y2="430"/>
    <line class="gridline" x1="258" x2="1094" y1="454.6" y2="454.6"/>
    <line class="gridline" x1="258" x2="1094" y1="479.3" y2="479.3"/>
    <line class="gridline" x1="258" x2="1094" y1="503.9" y2="503.9"/>
    <line class="gridline" x1="258" x2="1094" y1="528.6" y2="528.6"/>
    <line class="gridline" x1="258" x2="1094" y1="553.2" y2="553.2"/>
    <line class="gridline" x1="258" x2="1094" y1="577.9" y2="577.9"/>
    <line class="gridline" x1="258" x2="1094" y1="602.5" y2="602.5"/>
    <line class="gridline" x1="258" x2="1094" y1="627.2" y2="627.2"/>
    <line class="gridline" x1="258" x2="1094" y1="651.8" y2="651.8"/>
    <line class="gridline" x1="258" x2="1094" y1="676.5" y2="676.5"/>
  </g>

  <g class="ticks">
    <text class="tick-label" x="209" y="236">1800</text>
    <text class="tick-label" x="209" y="289">1600</text>
    <text class="tick-label" x="209" y="342">1400</text>
    <text class="tick-label" x="209" y="396">1200</text>
    <text class="tick-label" x="209" y="449">1000</text>
    <text class="tick-label" x="209" y="503">800</text>
    <text class="tick-label" x="209" y="556">600</text>
    <text class="tick-label" x="209" y="610">400</text>
    <text class="tick-label" x="209" y="663">200</text>
  </g>

  <g class="bars">
    <polygon fill="url(#fill-excellent)" points="304,701 304,631 367.5,586 431,631 431,701"/>
    <polygon fill="url(#fill-very-good)" points="458,701 458,561 522,522 586,561 586,701"/>
    <polygon fill="url(#fill-good)" points="613,701 613,503 676.5,459 740,503 740,701"/>
    <polygon fill="url(#fill-fair)" points="767,701 767,411 831,363 895,411 895,701"/>
    <polygon fill="url(#fill-poor)" points="922,701 922,307 985.5,258 1049,307 1049,701"/>
  </g>

  <line class="baseline" x1="258" x2="1095" y1="703" y2="703"/>

  <g class="values">
    <text class="value-label" x="369" y="577" text-anchor="middle" fill="url(#fill-excellent)">502</text>
    <text class="value-label" x="525" y="511" text-anchor="middle" fill="url(#fill-very-good)">661</text>
    <text class="value-label" x="678" y="450" text-anchor="middle" fill="url(#fill-good)">895</text>
    <text class="value-label" x="832" y="352" text-anchor="middle" fill="url(#fill-fair)">1268</text>
    <text class="value-label" x="980" y="241" text-anchor="middle" fill="url(#fill-poor)">1655</text>
  </g>

  <path class="trend" d="M305,465 C325,446 345,432 367,419 C415,390 470,376 522,366 C575,356 625,342 676,321 C740,294 790,256 831,218 C880,175 930,136 985,108"/>
  <g class="points">
    <circle cx="367" cy="419" r="11" fill="var(--excellent)"/>
    <circle cx="522" cy="366" r="11" fill="var(--very-good)"/>
    <circle cx="676" cy="321" r="11" fill="var(--good)"/>
    <circle cx="831" cy="218" r="11" fill="#6a14e6"/>
    <circle cx="985" cy="108" r="11" fill="#8a1fa8"/>
  </g>

  <g class="categories">
    <rect x="304" y="721" width="127" height="36" fill="var(--excellent)"/>
    <text class="category-label" x="367.5" y="749" text-anchor="middle">Excellent</text>
    <rect x="458" y="721" width="128" height="36" fill="var(--very-good)"/>
    <text class="category-label" x="522" y="747" text-anchor="middle">Very good</text>
    <rect x="613" y="721" width="127" height="36" fill="var(--good)"/>
    <text class="category-label" x="676.5" y="749" text-anchor="middle">Good</text>
    <rect x="767" y="721" width="128" height="36" fill="var(--fair)"/>
    <text class="category-label" x="831" y="749" text-anchor="middle">Fair</text>
    <rect x="922" y="721" width="127" height="36" fill="var(--poor)"/>
    <text class="category-label" x="985.5" y="749" text-anchor="middle">Poor</text>
  </g>

  <g class="axis-left">
    <text class="axis-acronym" transform="translate(107,406) rotate(-90)" text-anchor="middle">SAW-MX</text>
    <text class="axis-name" transform="translate(142,406) rotate(-90)" text-anchor="middle">(Self-Assessed Wellbeing Index for Movement Conditions)</text>
    <line class="axis-rule" x1="159" x2="159" y1="107" y2="706"/>
  </g>

  <text class="axis-right" transform="translate(1169,429) rotate(-90)" text-anchor="middle">QUALITY OF LIFE</text>
  <text class="axis-bottom" x="600" y="824" text-anchor="middle">Years Since Diagnosis</text>
</svg>
</main>
</body>
</html>
```